Building Maintenance Flyer specialising in hot and silent pressure cleaning

Hi. I love this flyer. I would like something similar but with hot water pressure washing and building maintenance

Ferro Lane & Services provides high pressure steam cleaning and water blasting services throughout Brisbane and surrounding areas, covering the Industrial, Commercial, Strata and Residential property owners sectors.

FLS combining the cleaning power of heat with state-of-the-art silent equipment, accredited technicians and a steadfast commitment to the environment. We offer the best Prompt, Professional Service.

Fully Accredited & Certified Technicians
100% Satisfaction Guaranteed
We are a family owned and operated business and love what we do. No job is too big or too small and we take pride in our work.
All of our services are undertaken using industry leading equipment and, providing safe and superior results.

Our business is covered by 20 million full public liability insurance and we operate within strict health & safety guidelines, providing all our clients with complete peace of mind. Project plans and risk assessments can also be provided upon request.

BODY CORPORATES

BUILDING FAÇADE CLEANING

CAR PARKS – underground, single and multi level

DRIVE THRU

FOOD PRODUCTION FACILITIES CLEANING SANITISING

SHOPPING CENTRES

BIRD MANAGEMENT AND DECONTAMINATION

GENERAL MAINTENANCE

CONSTRUCTION CLEAN UPS

SPILL MANAGEMENT

CONCRETE CLEANING AND DEGRASING

CONCRETE SEALING

FACTORY CLEANING & CLEAN UP

ENVIRONMENTAL DECONTAMINATION OF HEAVY VEHICLES AND EQUIPMENT

SITE CLEANS AND RUBBISH REMOVAL

MANUFACTURING PLANTS

Target Market(s)

Facility Managers, Commercial and Industrial Property Owners, Property Managers, Schools, Restaurants,

Industry/Entity Type

Pressure Cleaning

Font styles to use
Sans Serif

Colors
0293ce
00a990
33a6d7
33b8a4

Requirements
Must have
• SILENT HOT WATER PRESSURE CLEANING
Runs up to 120 Degrees Celsius
SANITISING - Bin areas, outdoor areas, cafe's, restaurants, schools, drive thru's
Blue's and Greens to link in with our logo

```html
<!DOCTYPE html>
<html lang="en">
<head>
<meta charset="utf-8">
<title>Ferro Lane &amp; Services – Property Maintenance Flyer</title>
<link rel="stylesheet" href="https://fonts.googleapis.com/css2?family=Montserrat:wght@300;400;500;600;700;800&display=swap">
<style>
  :root{
    --teal:#17a9b0;
    --teal-deep:#0f9aa1;
    --blue:#1d4fa8;
    --blue-deep:#163d8a;
    --ink:#1f1f1f;
    --dark-band:#2b2b2b;
    --page:#e6e6e6;
    --white:#ffffff;
    --contact-tint:#b8cbea;
  }
  *{box-sizing:border-box;margin:0;padding:0}
  html,body{width:800px;height:1200px;overflow:hidden;background:var(--page)}
  body{font-family:"Montserrat",sans-serif;color:var(--ink);position:relative}

  .flyer{
    position:absolute;left:10px;top:324px;
    width:1092px;height:772px;
    transform:scale(0.7143);transform-origin:0 0;
    overflow:hidden;background:var(--white);
    box-shadow:0 6px 14px rgba(0,0,0,.25);
  }
  .site-photo{
    position:absolute;left:0;top:0;width:760px;height:480px;
    background:linear-gradient(180deg,#cfe0ea 0%,#9fb7a8 30%,#6f8f6a 45%,#b9c0c4 62%,#8e9aa3 100%);
  }
  .shapes{position:absolute;left:0;top:0;width:1092px;height:772px}
  .technician-photo{
    position:absolute;left:895px;top:362px;width:197px;height:410px;
    border-radius:95px 95px 0 0;
    background:linear-gradient(180deg,#d9b49a 0%,#d9b49a 22%,#8e2a37 30%,#8e2a37 45%,#2f55b3 55%,#1f3f8e 100%);
  }

  .brand{
    position:absolute;left:712px;top:42px;width:200px;
    display:flex;align-items:center;justify-content:center;gap:10px;
  }
  .brand-dot{width:18px;height:18px;border-radius:50%;background:var(--teal)}
  .brand-name{font-weight:800;font-size:44px;color:var(--blue);letter-spacing:1px}

  .headline{position:absolute;left:520px;top:130px;width:590px;text-align:center;line-height:1}
  .headline-lead{display:block;font-weight:400;font-size:42px;color:var(--ink)}
  .headline-main{display:block;font-weight:800;font-size:47px;color:var(--blue);margin-top:6px}
  .headline-big{display:block;font-weight:800;font-size:60px;color:var(--blue);margin-top:2px}
  .tagline{position:absolute;left:590px;top:304px;width:450px;text-align:center;font-weight:700;font-size:15px;line-height:1.3}
  .tagline-rule{position:absolute;left:775px;top:356px;width:76px;height:3px;background:var(--teal)}

  .features{position:absolute;left:595px;top:380px;list-style:none;width:320px}
  .feature{display:flex;align-items:center;gap:14px;font-weight:500;font-size:15.5px;line-height:1.25;margin-bottom:14px}
  .feature-icon{flex:none;width:44px;height:44px}
  .feature strong{color:var(--blue);font-weight:700}

  .solutions-title{position:absolute;left:40px;top:448px;width:310px;text-align:center;color:var(--white);font-weight:800;font-size:34px}
  .solutions-rule{position:absolute;left:166px;top:506px;width:58px;height:2px;background:var(--white)}
  .services{position:absolute;left:30px;top:536px;width:420px;display:grid;grid-template-columns:206px 206px;column-gap:0;row-gap:14px;list-style:none}
  .service{display:flex;align-items:flex-start;gap:10px;color:var(--white);font-weight:500;font-size:14px;line-height:1.2;height:38px}
  .service-icon{flex:none;width:24px;height:24px;margin-top:2px}

  .badge-text{position:absolute;left:352px;top:400px;width:100px;text-align:center;color:var(--white);line-height:1}
  .badge-percent{display:block;font-weight:600;font-size:31px}
  .badge-sub{display:block;font-size:8px;margin-top:3px}
  .badge-strong{display:block;font-weight:700;font-size:10px;margin-top:3px}

  .contact{position:absolute;left:520px;top:620px;list-style:none}
  .contact-item{display:flex;align-items:center;gap:12px;font-size:15px;font-weight:500;margin-bottom:15px}
  .contact-phone{font-size:40px;font-weight:500;margin-bottom:10px}
  .contact-icon{flex:none;width:22px;height:22px}
  .contact-phone .contact-icon{width:26px;height:26px}
</style>
</head>
<body>
<article class="flyer">
  <div class="site-photo" role="img" aria-label="Photo of a technician in a hard hat and hi-vis vest turning a valve at an industrial pipe plant"></div>

  <svg class="shapes" viewBox="0 0 1092 772" aria-hidden="true">
    <defs>
      <linearGradient id="panelFade" x1="0" y1="0" x2="0" y2="1">
        <stop offset="0.45" stop-color="#ffffff"/>
        <stop offset="0.75" stop-color="#e4e4e4"/>
      </linearGradient>
      <linearGradient id="contactFade" x1="0" y1="0" x2="1" y2="0">
        <stop offset="0.45" stop-color="#ffffff"/>
        <stop offset="1" stop-color="#b8cbea"/>
      </linearGradient>
    </defs>
    <path d="M680,0 L760,0 C570,110 470,250 470,420 L420,430 C410,240 510,90 680,0 Z" fill="var(--blue)"/>
    <path d="M735,0 L1092,0 L1092,772 L500,772 C475,600 465,480 475,400 C490,220 590,80 735,0 Z" fill="url(#panelFade)"/>
    <path d="M440,460 C490,500 520,545 540,600 L512,606 C495,555 465,515 425,485 Z" fill="var(--dark-band)"/>
    <path d="M0,440 C90,385 260,370 390,410 C470,440 500,560 480,780 L0,780 Z" fill="var(--teal)" stroke="var(--white)" stroke-width="14"/>
    <path d="M500,772 C520,660 515,600 500,560 C640,590 860,595 1092,480 L1092,772 Z" fill="url(#contactFade)"/>
    <path d="M420,548 C620,588 860,592 1092,472" fill="none" stroke="var(--teal)" stroke-width="6"/>
    <path d="M330,425 L300,432 L318,440 L306,452 L345,445 Z" fill="var(--blue)"/>
    <path d="M474,425 L504,432 L486,440 L498,452 L459,445 Z" fill="var(--blue)"/>
    <circle cx="402" cy="432" r="62" fill="var(--blue)"/>
    <circle cx="402" cy="432" r="53" fill="none" stroke="var(--white)" stroke-width="2"/>
    <circle cx="402" cy="432" r="48" fill="var(--blue-deep)"/>
  </svg>

  <div class="technician-photo" role="img" aria-label="Photo of a smiling plumber in red shirt and blue overalls holding a pipe wrench"></div>

  <div class="brand">
    <span class="brand-dot"></span>
    <span class="brand-name">FLS</span>
  </div>

  <h1 class="headline">
    <span class="headline-lead">All Commercial &amp;</span>
    <span class="headline-main">Industrial Property</span>
    <span class="headline-big">Maintenance</span>
  </h1>
  <p class="tagline">FLS-servicing Southeast’s Commercial &amp; Industrial sector 24/7</p>
  <div class="tagline-rule"></div>

  <ul class="features">
    <li class="feature">
      <svg class="feature-icon" viewBox="0 0 44 44"><circle cx="22" cy="22" r="20" fill="none" stroke="var(--teal)" stroke-width="3"/><circle cx="22" cy="22" r="13" fill="var(--blue)"/><path d="M16,22 a6,6 0 1 1 6,6" fill="none" stroke="#fff" stroke-width="2"/></svg>
      <span>We operate 24/7, 7 days a week</span>
    </li>
    <li class="feature">
      <svg class="feature-icon" viewBox="0 0 44 44"><circle cx="22" cy="22" r="20" fill="none" stroke="var(--teal)" stroke-width="3"/><circle cx="22" cy="22" r="13" fill="var(--blue)"/><circle cx="22" cy="19" r="4" fill="#fff"/><path d="M15,29 q7,-8 14,0" fill="#fff"/></svg>
      <span><strong>SILENT HOT WATER PRESSURE CLEANING</strong> Runs up to 120 Degrees Celsius</span>
    </li>
    <li class="feature">
      <svg class="feature-icon" viewBox="0 0 44 44"><circle cx="22" cy="22" r="20" fill="none" stroke="var(--teal)" stroke-width="3"/><circle cx="22" cy="22" r="13" fill="var(--blue)"/><path d="M16,21 h4 v9 h-4 z M21,21 l4,-7 v7 h5 v9 h-9 z" fill="#fff"/></svg>
      <span>COVID-19 Trained</span>
    </li>
  </ul>

  <div class="badge-text">
    <span class="badge-percent">100%</span>
    <span class="badge-sub">Satisfaction</span>
    <span class="badge-strong">Guaranteed</span>
  </div>

  <h2 class="solutions-title">Solutions For</h2>
  <div class="solutions-rule"></div>
  <ul class="services">
    <li class="service"><svg class="service-icon" viewBox="0 0 24 24"><path d="M4,20 L16,8 M13,5 l6,6" stroke="#fff" stroke-width="2" fill="none"/></svg><span>COVID-19 Infection Control</span></li>
    <li class="service"><svg class="service-icon" viewBox="0 0 24 24"><rect x="4" y="10" width="12" height="10" fill="none" stroke="#fff" stroke-width="2"/><path d="M18,2 v18" stroke="#fff" stroke-width="2"/></svg><span>Common Area Cleaning</span></li>
    <li class="service"><svg class="service-icon" viewBox="0 0 24 24"><rect x="3" y="6" width="18" height="14" fill="none" stroke="#fff" stroke-width="2"/><path d="M8,11 h3 M13,11 h3 M8,15 h3 M13,15 h3" stroke="#fff" stroke-width="2"/></svg><span>Building Manage-<br>ment</span></li>
    <li class="service"><svg class="service-icon" viewBox="0 0 24 24"><path d="M6,20 L14,6 l4,2 -6,12 z" fill="#fff"/></svg><span>Bird waste removal</span></li>
    <li class="service"><svg class="service-icon" viewBox="0 0 24 24"><rect x="7" y="6" width="10" height="15" fill="none" stroke="#fff" stroke-width="2"/><path d="M5,6 h14" stroke="#fff" stroke-width="2"/></svg><span>Bin Cleaning &amp; Sani-<br>tisation</span></li>
    <li class="service"><svg class="service-icon" viewBox="0 0 24 24"><path d="M3,3 h18 v18 h-18 z M9,3 v18 M15,3 v18 M3,9 h18 M3,15 h18" fill="none" stroke="#fff" stroke-width="2"/></svg><span>Mould &amp; Mildew re-<br>moval</span></li>
    <li class="service"><svg class="service-icon" viewBox="0 0 24 24"><path d="M6,21 v-8 M3,13 h6 M14,21 v-6 a3,3 0 0 1 6,0 v6" fill="none" stroke="#fff" stroke-width="2"/></svg><span>Garden Mainte-<br>nance</span></li>
    <li class="service"><svg class="service-icon" viewBox="0 0 24 24"><rect x="6" y="3" width="12" height="18" rx="2" fill="#fff"/><circle cx="12" cy="12" r="2.5" fill="var(--teal)"/></svg><span>Oil and Grease elim-<br>ination</span></li>
  </ul>

  <ul class="contact">
    <li class="contact-item contact-phone">
      <svg class="contact-icon" viewBox="0 0 24 24"><path d="M6,2 l4,4 -2,3 q2,5 7,7 l3,-2 4,4 -3,3 q-10,0 -16,-13 z" fill="var(--blue)"/></svg>
      <span>0487 210 356</span>
    </li>
    <li class="contact-item">
      <svg class="contact-icon" viewBox="0 0 24 24"><circle cx="12" cy="12" r="10" fill="var(--blue)"/><path d="M2,12 h20 M12,2 q-6,10 0,20 M12,2 q6,10 0,20" fill="none" stroke="#fff" stroke-width="1.4"/></svg>
      <span>www.ferrolaneservices.com</span>
    </li>
    <li class="contact-item">
      <svg class="contact-icon" viewBox="0 0 24 24"><rect x="1" y="5" width="22" height="15" fill="var(--blue)"/><path d="M1,5 l11,8 11,-8" fill="none" stroke="#fff" stroke-width="1.6"/></svg>
      <span>hello@ferrolaneservices.com</span>
    </li>
  </ul>
</article>
</body>
</html>
```